Letterhead Design Project for online gaming site

We need a letterhead for a new online gaming company. The site is www.lunorapick.co

The logo is a gold colour and the site is similar in nature. Feel free to take a look at the landing page.

However the designer has free reign to do whatever they like with it.

OTHER CONTENT:

Telephone: 1300 617 385
Email: info@lunorapick.co
Web: www.lunorapick.co

Industry/Entity Type

It Company

```html
<!DOCTYPE html>
<html lang="en">
<head>
<meta charset="utf-8">
<title>LunoraPick.co Letterhead</title>
<link rel="stylesheet" href="https://fonts.googleapis.com/css2?family=Source+Sans+3:wght@400;700&family=Cinzel:wght@400&display=swap">
<style>
  :root {
    --paper: #ffffff;
    --paper-shade: #f3f3f3;
    --gold: #c9a020;
    --gold-deep: #a9821f;
    --gold-bright: #f1cf17;
    --ink: #2b2b2b;
    --swoosh: #3a3a3a;
    --silhouette: #e4e4e4;
  }
  html, body {
    margin: 0;
    padding: 0;
    width: 961px;
    height: 1200px;
    overflow: hidden;
    background: var(--paper);
  }
  .letterhead {
    position: relative;
    width: 961px;
    height: 1200px;
    background: linear-gradient(165deg, var(--paper) 0%, var(--paper-shade) 45%, var(--paper) 100%);
    font-family: "Source Sans 3", Arial, sans-serif;
    color: var(--ink);
  }
  .brand-name {
    position: absolute;
    left: 58px;
    top: 62px;
    margin: 0;
    font-size: 64px;
    font-weight: 700;
    line-height: 1;
    color: var(--gold);
    letter-spacing: -0.5px;
  }
  .contact-line {
    position: absolute;
    left: 78px;
    top: 150px;
    margin: 0;
    font-size: 17px;
    line-height: 1;
  }
  .contact-label {
    color: var(--gold-deep);
    font-weight: 700;
  }
  .contact-divider {
    color: var(--gold-deep);
    margin: 0 12px;
  }
  .racing-scene {
    position: absolute;
    left: 145px;
    top: 880px;
    width: 800px;
    height: 260px;
    background: radial-gradient(ellipse at 45% 60%, var(--silhouette) 0%, rgba(228,228,228,0.6) 45%, rgba(255,255,255,0) 75%);
  }
  .footer-band {
    position: absolute;
    left: 0;
    top: 1000px;
    width: 961px;
    height: 200px;
    display: block;
  }
  .site-address {
    position: absolute;
    right: 34px;
    top: 1148px;
    margin: 0;
    font-family: "Cinzel", "Times New Roman", serif;
    font-size: 17px;
    letter-spacing: 5px;
    color: var(--ink);
  }
</style>
</head>
<body>
  <main class="letterhead">
    <h1 class="brand-name">LunoraPick.co</h1>
    <p class="contact-line">
      <span class="contact-label">T:</span> 1300 617 385
      <span class="contact-divider">|</span>
      <span class="contact-label">E:</span> info@lunorapick.co
    </p>

    <div class="racing-scene" role="img" aria-label="Faint grey silhouettes of a harness racer, a galloping jockey and two greyhounds"></div>

    <svg class="footer-band" viewBox="0 0 961 200" aria-hidden="true">
      <defs>
        <linearGradient id="band-gold" x1="0" y1="0" x2="1" y2="0">
          <stop offset="0" stop-color="var(--gold-deep)"/>
          <stop offset="0.5" stop-color="var(--gold-bright)"/>
          <stop offset="1" stop-color="var(--gold-deep)"/>
        </linearGradient>
        <linearGradient id="swoosh-fade" x1="0" y1="0" x2="1" y2="0">
          <stop offset="0" stop-color="var(--swoosh)"/>
          <stop offset="0.45" stop-color="#9a9a9a"/>
          <stop offset="1" stop-color="var(--swoosh)"/>
        </linearGradient>
      </defs>
      <path class="band-swoosh" d="M0 138 C 160 168, 380 178, 560 138 S 860 74, 961 62 L 961 70 C 860 82, 720 118, 560 148 S 160 176, 0 150 Z" fill="url(#swoosh-fade)"/>
      <path class="band-gold" d="M0 152 C 160 180, 380 182, 560 150 S 860 84, 961 72 L 961 200 L 0 200 Z" fill="url(#band-gold)"/>
    </svg>

    <p class="site-address">WWW.LUNORAPICK.CO</p>
  </main>
</body>
</html>
```